Attention grabbing 6x9 postcard

We are looking to have an attention grabbing post card that be sent out to homeowners from our roofing company Olum Roofing. the concept is that on the front it will say something like (STOP THE KNOCKING!
Tired of roofers knocking on your door? Contact us because we value your time as much as you value the roof over your head."
Olum Roofing
OlumRoofing.com
877.612.OLUM
info@olumroofing.com

Please feel free to come up with something very creative. Once we pick the final design we will provide the copy.

```html
<!DOCTYPE html>
<html lang="en">
<head>
<meta charset="utf-8">
<title>Olum Roofing Postcard</title>
<link rel="stylesheet" href="https://fonts.googleapis.com/css2?family=Oswald:wght@700&family=Open+Sans:wght@400;600;700&display=swap">
<style>
  :root {
    --backdrop: #f7c25e;
    --charcoal: #2a2a2a;
    --gold: #f2b035;
    --gold-deep: #e9a92c;
    --paper: #fbfbfb;
    --ink: #232323;
    --white: #ffffff;
  }
  * { margin: 0; padding: 0; box-sizing: border-box; }
  html, body { width: 1200px; height: 800px; overflow: hidden; }
  body {
    background: var(--backdrop);
    font-family: "Open Sans", Arial, sans-serif;
    position: relative;
  }
  .card {
    position: absolute;
    width: 441px;
    height: 667px;
    top: 66px;
    overflow: hidden;
  }
  .card--front { left: 128px; background: var(--gold); }
  .card--back { left: 632px; background: var(--paper); }

  .brand-mark {
    display: inline-flex;
    align-items: center;
    gap: 8px;
    font-weight: 700;
    letter-spacing: 1.5px;
    white-space: nowrap;
  }
  .brand-mark .dot {
    display: inline-block;
    width: 12px; height: 12px;
    border-radius: 50%;
    background: currentColor;
  }

  /* Front */
  .door-photo {
    position: absolute;
    left: 0; right: 0; top: 360px; bottom: 0;
    background: linear-gradient(180deg, #f0b436 0%, #e6a82c 100%);
  }
  .front-panel {
    position: absolute;
    left: 0; top: 0;
    width: 441px; height: 410px;
  }
  .front-brand {
    position: absolute;
    top: 46px; left: 0; right: 0;
    display: flex;
    justify-content: center;
    color: var(--gold);
    font-size: 19px;
  }
  .headline {
    position: absolute;
    top: 100px; left: 0; right: 0;
    text-align: center;
    color: var(--white);
    font-family: "Oswald", Impact, sans-serif;
    font-weight: 700;
    text-transform: uppercase;
    line-height: 0.88;
    letter-spacing: -1px;
  }
  .headline .line-1 { display: block; font-size: 76px; }
  .headline .line-2 { display: block; font-size: 82px; }
  .front-intro {
    position: absolute;
    top: 262px; left: 20px; right: 20px;
    text-align: center;
    color: var(--gold);
    font-weight: 600;
    font-size: 15.5px;
    line-height: 1.3;
  }
  .front-footer {
    position: absolute;
    left: 28px; bottom: 38px;
    width: 160px;
    display: flex;
    flex-direction: column;
    align-items: center;
    color: var(--ink);
  }
  .front-footer .brand-mark { font-size: 17px; margin-bottom: 10px; }
  .front-footer .site { font-weight: 400; font-size: 11.5px; letter-spacing: 0.5px; }

  /* Back */
  .back-brand {
    position: absolute;
    top: 56px; left: 30px;
    color: var(--ink);
    font-size: 15px;
  }
  .back-site {
    position: absolute;
    top: 89px; left: 31px;
    font-size: 9.5px;
    font-weight: 600;
    letter-spacing: 0.3px;
    color: var(--ink);
  }
  .back-rule {
    position: absolute;
    top: 108px; left: 29px;
    width: 379px; height: 2px;
    background: var(--gold);
  }
  .company-name {
    position: absolute;
    top: 130px; left: 29px;
    font-size: 26px;
    font-weight: 700;
    color: var(--ink);
    letter-spacing: 0.3px;
  }
  .contact-list {
    position: absolute;
    top: 180px; left: 29px;
    list-style: none;
    font-size: 14.5px;
    line-height: 19.5px;
    color: var(--ink);
  }
  .contact-list .label { display: inline-block; width: 36px; }
  .honeycomb-field {
    position: absolute;
    left: 0; right: 0; top: 300px; bottom: 0;
    background: linear-gradient(180deg, rgba(242,176,53,0) 0%, rgba(242,176,53,0.35) 25%, var(--gold) 55%, var(--gold-deep) 100%);
  }
  .back-cta {
    position: absolute;
    top: 536px; left: 20px; right: 20px;
    text-align: center;
    font-weight: 600;
    font-size: 17px;
    line-height: 1.27;
    color: var(--ink);
  }
</style>
</head>
<body>
  <section class="card card--front">
    <div class="door-photo" role="img" aria-label="Photo of a fist knocking on a yellow front door"></div>
    <svg class="front-panel" viewBox="0 0 441 410" aria-hidden="true">
      <polygon fill="#2a2a2a" points="0,0 441,0 441,380 406,403 352,375 310,400 231,363 167,403 112,375 60,403 0,366"/>
    </svg>
    <div class="front-brand"><span class="brand-mark"><span class="dot"></span>OLUM ROOFING</span></div>
    <h1 class="headline"><span class="line-1">Stop the</span><span class="line-2">Knocking!</span></h1>
    <p class="front-intro">Tired of roofers knocking on your door?<br>Contact us because we value your time as<br>much as you value the roof over your head</p>
    <div class="front-footer">
      <span class="brand-mark"><span class="dot"></span>OLUM ROOFING</span>
      <div class="site">OLUMROOFING.COM</div>
    </div>
  </section>

  <section class="card card--back">
    <div class="back-brand"><span class="brand-mark"><span class="dot"></span>OLUM ROOFING</span></div>
    <div class="back-site">OLUMROOFING.COM</div>
    <div class="back-rule"></div>
    <h2 class="company-name">OLUM ROOFING</h2>
    <ul class="contact-list">
      <li><span class="label">Visit</span>: OlumRoofing.com</li>
      <li><span class="label">Call</span>: 877.612.OLUM</li>
      <li><span class="label">Mail</span>: info@olumroofing.com</li>
    </ul>
    <div class="honeycomb-field" role="img" aria-label="Decorative honeycomb pattern fading into gold"></div>
    <p class="back-cta">Schedule your roofing consultation today<br>and enjoy peace of mind knowing you're in<br>good hands</p>
  </section>
</body>
</html>
```